New Zealand Export company needs business cards

We need new business cards to match our new logo for a company based in New Zealand who deal specifically with the Pacific Islands. We source, consolidate and ship products out of New Zealand to the Pacific Islands. Will attach our old ones and also new logo.
Would like the Islands we deal with and the areas of work we have access to, to be included on the business cards.

Contact Information for Business Card

T +64 9 571 3048
F +64 9 571 6285
12-18 Kowhai Lane, Drury, 2113
PO Box 814, Drury, Auckland 2247, New Zealand
www.falconfreight.example.nz
E sales@falconfreight.example.nz

Font styles to use
Sans Serif

Colors
85abd2
33a6d7
ffffff

Requirements
Must have
• A company of PWM

```html
<!DOCTYPE html>
<html lang="en">
<head>
<meta charset="utf-8">
<title>Falcon Freight – Business Card</title>
<link rel="stylesheet" href="https://fonts.googleapis.com/css2?family=Roboto:wght@400;500;700&display=swap">
<style>
  :root {
    --stage: #2b2d31;
    --brand-blue: #0f58a8;
    --sky-blue: #3bbfea;
    --paper: #ffffff;
    --ink: #333333;
  }
  * { box-sizing: border-box; margin: 0; padding: 0; }
  html, body { width: 1200px; height: 1000px; overflow: hidden; }
  body {
    background: var(--stage);
    font-family: "Roboto", Arial, sans-serif;
    position: relative;
  }
  .card {
    position: absolute;
    left: 215px;
    width: 770px;
    height: 440px;
    border-radius: 26px;
    overflow: hidden;
  }
  .card-front { top: 40px; background: var(--brand-blue); }
  .card-back { top: 520px; background: var(--paper); }

  .wordmark {
    position: absolute;
    display: flex;
    align-items: center;
    gap: 18px;
    white-space: nowrap;
  }
  .wordmark-square { display: block; flex: none; background: var(--sky-blue); }
  .wordmark-name { font-weight: 700; letter-spacing: 0.06em; line-height: 1; white-space: nowrap; }

  .card-front .wordmark { left: 50%; top: 50%; transform: translate(-50%, -50%); }
  .card-front .wordmark-square { width: 46px; height: 46px; }
  .card-front .wordmark-name { font-size: 54px; color: var(--paper); }

  .card-back .wordmark { left: 56px; top: 50px; }
  .card-back .wordmark-square { width: 30px; height: 30px; }
  .card-back .wordmark-name { font-size: 34px; color: var(--brand-blue); }

  .address {
    position: absolute;
    left: 58px;
    top: 112px;
    font-size: 19px;
    font-style: normal;
    line-height: 1.35;
    color: var(--ink);
  }
  .contacts {
    position: absolute;
    left: 58px;
    top: 196px;
    list-style: none;
    font-size: 19px;
    line-height: 1.45;
    color: var(--ink);
  }
  .contacts li { display: flex; align-items: center; gap: 10px; }
  .contacts svg { width: 16px; height: 16px; fill: var(--brand-blue); flex: none; }
  .contacts .web-name { color: var(--brand-blue); }

  .swoosh { position: absolute; inset: 0; width: 770px; height: 440px; }
  .parent-line {
    position: absolute;
    right: 60px;
    bottom: 30px;
    color: var(--paper);
    font-size: 24px;
    font-weight: 500;
    white-space: nowrap;
  }
</style>
</head>
<body>
  <section class="card card-front" aria-label="Card front">
    <div class="wordmark">
      <span class="wordmark-square"></span>
      <span class="wordmark-name">FALCON FREIGHT</span>
    </div>
  </section>

  <section class="card card-back" aria-label="Card back">
    <svg class="swoosh" viewBox="0 0 770 440" aria-hidden="true">
      <path d="M0 290 C220 350 520 340 770 220 L770 236 C520 360 220 366 0 308 Z" fill="var(--sky-blue)"/>
      <path d="M100 440 C320 400 580 350 770 256 L770 440 Z" fill="var(--brand-blue)"/>
    </svg>

    <div class="wordmark">
      <span class="wordmark-square"></span>
      <span class="wordmark-name">FALCON FREIGHT</span>
    </div>

    <address class="address">
      12-18 Kowhai Lane, Drury, 2113<br>
      PO Box 814, Drury, Auckland 2247,<br>
      New Zealand
    </address>

    <ul class="contacts">
      <li>
        <svg viewBox="0 0 24 24"><path d="M6.6 10.8a15.1 15.1 0 0 0 6.6 6.6l2.2-2.2c.3-.3.7-.4 1-.2 1.1.4 2.3.6 3.6.6.6 0 1 .4 1 1V20c0 .6-.4 1-1 1C10.6 21 3 13.4 3 4c0-.6.4-1 1-1h3.5c.6 0 1 .4 1 1 0 1.3.2 2.5.6 3.6.1.3 0 .7-.2 1z"/></svg>
        +64 9 571 3048
      </li>
      <li>
        <svg viewBox="0 0 24 24"><path d="M6 2h12v5H6zM3 8h18a1 1 0 0 1 1 1v8h-4v5H6v-5H2V9a1 1 0 0 1 1-1zm5 8v4h8v-4z"/></svg>
        +64 9 571 6285
      </li>
      <li>
        <svg viewBox="0 0 24 24"><path d="M2 5h20v14H2zm2 2v.5l8 5.5 8-5.5V7l-8 5.5z"/></svg>
        E sales@falconfreight.example.nz
      </li>
      <li>
        <svg viewBox="0 0 24 24"><path d="M12 2a10 10 0 1 0 0 20 10 10 0 0 0 0-20zm0 2a8 8 0 0 1 7.7 6h-3.9a12 12 0 0 0-2-5.8A8 8 0 0 1 12 4zM4.3 14h3.9a12 12 0 0 0 2 5.8A8 8 0 0 1 4.3 14zm0-4a8 8 0 0 1 5.9-5.8 12 12 0 0 0-2 5.8zm5.9 0a10 10 0 0 1 1.8-5 10 10 0 0 1 1.8 5zm0 4h3.6a10 10 0 0 1-1.8 5 10 10 0 0 1-1.8-5zm5.6 0h3.9a8 8 0 0 1-5.9 5.8 12 12 0 0 0 2-5.8z"/></svg>
        <span>www.<span class="web-name">falconfreight.example</span>.nz</span>
      </li>
    </ul>

    <p class="parent-line">A company of PWM</p>
  </section>
</body>
</html>
```